In Search of a FANTASTIC BUSINESS CARD REFRESH AND REDESIGN

I would like to redesign the current business card for my company.  There is a parent company, Brookfane Care Group, with 2 operating companies - Brookfane Homecare and Brookfane Senior Living.
I will include the current business card design, along with the 3 logos I would like incorporated.  The business card can be two sided.  I'm looking for something clean, professional, and a fresh new look.

Target Market(s)
Hospitals, social workers, insurance agents, family members of seniors
Industry/Entity Type
Healthcare
Contact Information for Business Card
Name, title of person, address, phone number, web address, email address
Look and feel
Each slider illustrates characteristics of the customer's brand and the style your logo design should communicate.

```html
<!DOCTYPE html>
<html lang="en">
<head>
<meta charset="utf-8">
<title>Brookfane Homecare – Business Card</title>
<link href="https://fonts.googleapis.com/css2?family=Ubuntu:wght@400;500;700&display=swap" rel="stylesheet">
<style>
  :root {
    --bg: #dcdde0;
    --coral-dark: #cf716f;
    --coral-light: #f29f9a;
    --coral: #e0676a;
    --white: #ffffff;
    --ink: #55575b;
    --ink-soft: #5f6165;
    --wordmark: #6a6a6c;
    --teal: #5d9e9c;
    --black: #1a1a1a;
  }
  * { margin: 0; padding: 0; box-sizing: border-box; }
  html, body { width: 1200px; height: 800px; overflow: hidden; }
  body {
    background: var(--bg);
    font-family: "Ubuntu", sans-serif;
    position: relative;
  }
  .card {
    position: absolute;
    left: 390px;
    width: 420px;
    height: 240px;
    border-radius: 20px;
    overflow: hidden;
  }
  .card--front {
    top: 130px;
    background: linear-gradient(225deg, var(--coral-light) 0%, var(--coral-dark) 100%);
  }
  .card--back {
    top: 430px;
    background: linear-gradient(135deg, #f4f4f4 0%, #ececec 50%, #fafafa 100%);
  }

  /* Front */
  .front-brand {
    position: absolute;
    left: 0; right: 0; top: 56px;
    display: flex;
    flex-direction: column;
    align-items: center;
    gap: 12px;
  }
  .brand-square {
    width: 54px; height: 54px;
    background: var(--white);
    border-radius: 8px;
  }
  .front-brand__name {
    font-size: 36px;
    font-weight: 500;
    color: var(--wordmark);
    text-align: center;
    line-height: 1.05;
    letter-spacing: -0.3px;
  }

  /* Back */
  .sister-brands {
    position: absolute;
    top: 26px; right: 26px;
    display: flex;
    gap: 18px;
  }
  .sister-brand {
    display: flex;
    flex-direction: column;
    align-items: center;
    gap: 7px;
    width: 86px;
    text-align: center;
  }
  .sister-brand__square {
    width: 24px; height: 24px;
    border-radius: 4px;
  }
  .sister-brand__name {
    font-size: 12px;
    font-weight: 500;
    line-height: 1.2;
  }
  .sister-brand--living .sister-brand__square { background: var(--teal); }
  .sister-brand--living .sister-brand__name { color: var(--teal); }
  .sister-brand--group .sister-brand__square { background: var(--black); }
  .sister-brand--group .sister-brand__name { color: var(--black); }

  .person {
    position: absolute;
    left: 35px; top: 120px;
  }
  .person__name {
    font-size: 21px;
    color: var(--ink);
    letter-spacing: 0.2px;
    line-height: 1.1;
  }
  .person__name strong { font-weight: 700; }
  .person__title {
    font-size: 15px;
    color: var(--coral);
    margin-top: 3px;
  }
  .divider {
    position: absolute;
    left: 36px; right: 30px; top: 171px;
    height: 2px;
    background: var(--coral);
  }
  .contacts {
    position: absolute;
    left: 36px; right: 28px; top: 186px;
    display: flex;
    justify-content: space-between;
    font-size: 10.5px;
    color: var(--ink-soft);
    line-height: 13px;
  }
  .contacts__col { display: flex; flex-direction: column; }
  .contact-line { display: flex; align-items: center; gap: 4px; white-space: nowrap; }
  .contact-line svg { width: 8px; height: 8px; flex: none; }
  .contacts__address .contact-line { align-items: flex-start; }
  .contacts__address svg { margin-top: 2px; }
</style>
</head>
<body>

  <section class="card card--front" aria-label="Card front">
    <div class="front-brand">
      <div class="brand-square"></div>
      <div class="front-brand__name">Brookfane<br>Homecare</div>
    </div>
  </section>

  <section class="card card--back" aria-label="Card back">
    <div class="sister-brands">
      <div class="sister-brand sister-brand--living">
        <div class="sister-brand__square"></div>
        <div class="sister-brand__name">Brookfane<br>Senior Living</div>
      </div>
      <div class="sister-brand sister-brand--group">
        <div class="sister-brand__square"></div>
        <div class="sister-brand__name">Brookfane<br>Care Group</div>
      </div>
    </div>

    <div class="person">
      <div class="person__name">MAREN <strong>BROOKFANE</strong></div>
      <div class="person__title">President, CEO</div>
    </div>

    <div class="divider"></div>

    <div class="contacts">
      <div class="contacts__col">
        <div class="contact-line">
          <svg viewBox="0 0 10 10"><path d="M2 1 L3.8 1 L4.3 3 L3.2 3.8 Q4 5.8 6.2 6.8 L7 5.7 L9 6.2 L9 8 Q9 9 8 9 Q1 8.5 1 2 Q1 1 2 1Z" fill="none" stroke="#e0676a" stroke-width="0.9"/></svg>
          (808) 555-0142
        </div>
        <div class="contact-line">
          <svg viewBox="0 0 10 10"><rect x="3" y="1" width="4" height="3" fill="#e0676a"/><rect x="1" y="4" width="8" height="3.5" rx="0.6" fill="#e0676a"/><rect x="3" y="6.5" width="4" height="2.5" fill="#e0676a"/></svg>
          (808) 555-0187
        </div>
      </div>
      <div class="contacts__col">
        <div class="contact-line">
          <svg viewBox="0 0 10 10"><rect x="1" y="2.5" width="8" height="5.5" fill="#e0676a"/><path d="M1 2.5 L5 5.5 L9 2.5" fill="none" stroke="#fff" stroke-width="0.8"/></svg>
          Maren@brookfanecare.com
        </div>
        <div class="contact-line">
          <svg viewBox="0 0 10 10"><circle cx="5" cy="5" r="4" fill="none" stroke="#e0676a" stroke-width="0.9"/><path d="M1 5 H9 M5 1 Q2.5 5 5 9 M5 1 Q7.5 5 5 9" fill="none" stroke="#e0676a" stroke-width="0.7"/></svg>
          www.brookfanecare.com
        </div>
      </div>
      <div class="contacts__col contacts__address">
        <div class="contact-line">
          <svg viewBox="0 0 10 10"><path d="M5 9.5 Q1.5 5.5 1.5 3.7 A3.5 3.5 0 0 1 8.5 3.7 Q8.5 5.5 5 9.5Z" fill="none" stroke="#e0676a" stroke-width="0.9"/><circle cx="5" cy="3.7" r="1.2" fill="#e0676a"/></svg>
          <span>480 Lanakila Ave, Suite<br>210, Honolulu, HI 96817</span>
        </div>
      </div>
    </div>
  </section>

</body>
</html>
```